Redesign the CTA buttons and scheenshots

https://www.plomvra.com/design/kT7wPqz2LmX9nBv4HsYcRe/04122024-Basketlyn-Final-v5?node-id=46-40225&t=ab3xk9Lm2QpVwZr7-1
Basketlyn is a collaborative shopping app that brings everything into one place.
Users can shop with friends and family and make product decisions together instead of shopping alone.

I’m redesigning the app’s action buttons (CTAs) and the App Store screenshots to improve clarity, engagement, and conversion. I’ve provided example App Store pages and competitor links for reference.

In Figma, I’ve highlighted the specific buttons and areas that need attention, along with clear instructions and context for each change.

If you see opportunities to improve any app buttons or strengthen the call-to-action, please review those areas and submit your suggested improvements.

Industry/Entity Type

Social Shopping

Number of Pages Required

1 page

Font styles to use
Other font styles liked:
• Use our Color Legend

Requirements
Must have
• Screenshots for the app store and New users and signed up users

```html
<!DOCTYPE html>
<html lang="en">
<head>
<meta charset="utf-8">
<title>Basketlyn – app screens</title>
<link rel="stylesheet" href="https://fonts.googleapis.com/css2?family=Inter:wght@400;500;600;700;800&display=swap">
<style>
:root{
  --stage:#1b1b1c;
  --brand:#4a33d8;
  --brand-deep:#3a26b8;
  --mint:#5fe6d0;
  --mint-soft:#c9f7ef;
  --sun:#f9d64a;
  --ink:#151515;
  --muted:#3c3c3c;
  --line:#e3e3e8;
  --card:#ffffff;
  --star:#f6c533;
}
*{box-sizing:border-box;margin:0;padding:0}
html,body{width:1200px;height:888px;overflow:hidden}
body{background:var(--stage);font-family:"Inter",Helvetica,Arial,sans-serif;color:var(--ink);position:relative}
.screen{position:absolute;width:243px;background:#fff;overflow:hidden;display:flex;flex-direction:column}
.screen--wishlist-clip{left:45px;top:75px;height:535px;border-radius:18px}
.screen--wishlist{left:340px;top:63px;height:769px}
.screen--stores{left:621px;top:63px;height:535px}
.screen--discover{left:901px;top:62px;height:432px}

.app-bar{height:35px;flex:none;background:var(--brand);display:flex;align-items:center;padding:0 8px;gap:7px}
.app-bar .title{color:#fff;font-size:12.5px;font-weight:500}
.round{width:16px;height:16px;border-radius:50%;background:var(--mint);display:flex;align-items:center;justify-content:center;flex:none}
.round svg{width:10px;height:10px;stroke:var(--brand);fill:none;stroke-width:2.4;stroke-linecap:round;stroke-linejoin:round}
.bar-actions{margin-left:auto;display:flex;gap:7px}

.body{flex:1;overflow:hidden;padding:0 7px}
.event-row{display:flex;justify-content:space-between;align-items:baseline;padding:11px 1px 6px}
.event-row h2{font-size:10.5px;font-weight:500}
.event-row h2 sup{font-size:6px}
.event-row span{font-size:8.5px;color:var(--muted)}
.hero{height:88px;border-radius:4px;background:linear-gradient(90deg,#78b2cc 0%,#8cc0d6 55%,#a9d2e2 100%);position:relative;padding:15px 14px;color:#fff}
.hero .cake{position:absolute;right:40px;top:10px;width:80px;height:78px;border-radius:6px 6px 0 0;background:linear-gradient(180deg,rgba(255,255,255,.0),rgba(255,240,230,.55))}
.hero h3{font-size:9.5px;font-weight:700;line-height:1.3;width:100px}
.hero p{font-size:7px;line-height:1.25;width:90px;margin-top:6px}

.grid{display:grid;grid-template-columns:1fr 1fr;gap:10px;margin-top:11px}
.col{display:flex;flex-direction:column;gap:8px}
.add-wishlist{background:var(--mint);border-radius:5px;height:117px;display:flex;flex-direction:column;align-items:center;padding-top:14px;text-align:center}
.add-wishlist p{font-size:9px;line-height:1.4}
.add-wishlist .plus{width:23px;height:23px;border-radius:50%;background:#1e1e1e;margin:10px 0 9px;display:flex;align-items:center;justify-content:center}
.add-wishlist .plus svg{width:12px;height:12px;stroke:var(--mint);stroke-width:3;stroke-linecap:round}
.add-wishlist strong{font-size:9.5px;font-weight:500}

.product-card{border:1px solid var(--line);border-radius:5px;padding:6px 5px 5px;position:relative}
.product-card .more{position:absolute;right:6px;top:8px;width:2px;height:10px;background:radial-gradient(circle,#111 1px,transparent 1.3px) 0 0/2px 3.5px}
.product-shot{border-radius:3px;margin:4px 8px 8px}
.stars{color:var(--star);font-size:7px;letter-spacing:1px;padding:0 3px}
.product-name{font-size:7.6px;line-height:1.4;color:var(--muted);padding:3px 3px 0}
.price{font-size:8.5px;padding:6px 3px 0}
.store{font-size:7.6px;padding:5px 3px 0}
.card-actions{display:flex;align-items:center;gap:6px;margin-top:7px;font-size:8px;color:var(--brand)}
.vote{display:flex;align-items:center;gap:2px;padding-left:3px}
.vote svg{width:8px;height:8px;stroke:var(--brand);fill:none;stroke-width:2}
.review-btn{margin-left:auto;background:var(--mint);border-radius:4px;padding:4px 5px;display:flex;gap:3px;align-items:center;color:var(--brand-deep);font-size:7.6px}
.review-btn svg{width:7px;height:7px;stroke:var(--brand-deep);fill:none;stroke-width:2}

.tab-bar{height:37px;flex:none;background:var(--brand);display:grid;grid-template-columns:52px 1fr 1fr 52px;font-size:8px;color:#fff}
.tab{display:flex;flex-direction:column;align-items:center;justify-content:center;gap:3px}
.tab svg{width:11px;height:11px;stroke:var(--mint);fill:none;stroke-width:2.2;stroke-linejoin:round;stroke-linecap:round}
.tab.is-active{background:var(--mint);color:var(--brand)}
.tab.is-active svg{stroke:var(--brand)}

.intro{border:1px solid var(--line);border-radius:5px;margin-top:12px;height:168px;text-align:center;padding:14px 12px 0}
.intro h2{font-size:12.5px;font-weight:800;color:var(--brand)}
.intro h3{font-size:11.5px;font-weight:400;margin-top:2px}
.intro p{font-size:8.3px;line-height:1.55;margin-top:10px}
.demo-btn{display:inline-flex;align-items:center;gap:8px;background:var(--sun);border-radius:9px;padding:7px 12px;margin-top:11px;font-size:10px;font-weight:500}
.demo-btn i{width:13px;height:13px;border-radius:50%;background:#111;display:flex;align-items:center;justify-content:center}
.demo-btn i::after{content:"";border-left:5px solid var(--sun);border-top:3px solid transparent;border-bottom:3px solid transparent;margin-left:1px}
.section-head{font-size:12px;font-weight:500;margin:18px 2px 9px}
.letter-head{font-size:12px;font-weight:600;margin:17px 2px 7px}
.brands{display:grid;grid-template-columns:repeat(4,1fr);gap:5px}
.brand-tile{border:1px solid var(--line);border-radius:5px;height:44px;display:flex;flex-direction:column;align-items:center;justify-content:center;gap:5px}
.brand-tile i{width:14px;height:14px;border-radius:50%;background:var(--c,#d94a3d)}
.brand-tile span{font-size:7.8px;color:var(--muted)}
.brands + .brands{margin-top:5px}

.search-band{height:38px;background:var(--mint);flex:none;padding:6px 7px}
.search-field{background:#fff;border-radius:13px;height:24px;display:flex;align-items:center;padding:0 11px;font-size:8px;color:var(--muted)}
.search-field svg{margin-left:auto;width:10px;height:10px;stroke:#111;fill:none;stroke-width:2}
.category{display:flex;justify-content:space-between;align-items:center;margin:14px 2px 7px}
.category h2{font-size:11.5px;font-weight:500}
.view-all{background:var(--mint-soft);border:1px solid var(--mint);border-radius:8px;font-size:7px;padding:2px 5px}
.group-row{display:flex;gap:7px;width:400px}
.group-card{width:105px;height:99px;border-radius:6px;position:relative;flex:none;color:#fff;padding:6px 8px}
.group-card .tag{position:absolute;left:8px;top:6px;background:var(--mint);color:#111;font-size:8px;border-radius:7px;padding:2px 6px}
.group-card .mark{position:absolute;right:6px;top:4px;width:6px;height:9px;background:#fff;clip-path:polygon(0 0,100% 0,100% 100%,50% 72%,0 100%)}
.members{position:absolute;left:8px;top:54px;display:flex;align-items:center;font-size:6.5px}
.members i{width:10px;height:10px;border-radius:50%;border:1px solid #fff;background:#c6d6ea;margin-right:-3px}
.members i:nth-child(2){background:#9fb3cf}
.members span{margin-left:6px}
.group-card p{position:absolute;left:8px;top:72px;font-size:7.3px;line-height:1.3}
.peek{width:14px;margin-right:-30px}
</style>
</head>
<body>
<svg width="0" height="0" style="position:absolute">
  <defs>
    <symbol id="i-back" viewBox="0 0 12 12"><path d="M7.5 2.5 4 6l3.5 3.5"/></symbol>
    <symbol id="i-info" viewBox="0 0 12 12"><path d="M6 5.5v4M6 2.7v.1"/></symbol>
    <symbol id="i-user" viewBox="0 0 12 12"><circle cx="5" cy="4" r="2"/><path d="M1.5 10c.5-2 2-3 3.5-3s3 1 3.5 3M9.5 3v3M8 4.5h3"/></symbol>
    <symbol id="i-chat" viewBox="0 0 12 12"><path d="M3 4h6M3 7h4"/></symbol>
    <symbol id="i-menu" viewBox="0 0 12 12"><path d="M3 3.5h6M3 6h6M3 8.5h6"/></symbol>
    <symbol id="i-up" viewBox="0 0 12 12"><path d="M1 5h2v6H1zM3 5l3-4c1 0 1.5.8 1.2 2L7 5h3c.8 0 1.2.7 1 1.4L10 10c-.2.6-.6 1-1.2 1H3"/></symbol>
    <symbol id="i-down" viewBox="0 0 12 12"><path d="M1 1h2v6H1zM3 7l3 4c1 0 1.5-.8 1.2-2L7 7h3c.8 0 1.2-.7 1-1.4L10 2c-.2-.6-.6-1-1.2-1H3"/></symbol>
    <symbol id="i-star" viewBox="0 0 12 12"><path d="M6 1l1.5 3.2 3.5.4-2.6 2.4.7 3.5L6 8.8 2.9 10.5l.7-3.5L1 4.6l3.5-.4z"/></symbol>
    <symbol id="i-home" viewBox="0 0 12 12"><path d="M1.5 5.5 6 1.5l4.5 4V10.5h-9z"/></symbol>
    <symbol id="i-store" viewBox="0 0 12 12"><path d="M1.5 4.5 2.5 1.5h7l1 3zM2 4.5v6h8v-6M5 10.5v-3h2v3"/></symbol>
    <symbol id="i-search" viewBox="0 0 12 12"><circle cx="5" cy="5" r="3.5"/><path d="m7.8 7.8 3 3"/></symbol>
    <symbol id="i-bubble" viewBox="0 0 12 12"><path d="M1.5 1.5h9v7h-5l-3 2v-2h-1zM3.5 4h5M3.5 6h3"/></symbol>
    <symbol id="i-plus" viewBox="0 0 12 12"><path d="M6 1v10M1 6h10"/></symbol>
  </defs>
</svg>

<!-- Wishlist screen, first view -->
<section class="screen screen--wishlist-clip">
  <header class="app-bar">
    <span class="round"><svg><use href="#i-back"/></svg></span>
    <span class="title">Basketlyn</span>
    <div class="bar-actions">
      <span class="round"><svg><use href="#i-info"/></svg></span>
      <span class="round"><svg><use href="#i-user"/></svg></span>
      <span class="round"><svg><use href="#i-chat"/></svg></span>
      <span class="round"><svg><use href="#i-menu"/></svg></span>
    </div>
  </header>
  <div class="body">
    <div class="event-row"><h2>Marco’s 30<sup>th</sup> Birthday</h2><span>@marcob</span></div>
    <div class="hero"><div class="cake" role="img" aria-label="Birthday cake with colourful candles"></div><h3>LOREM IPSUM IS SIMPLY DUM.</h3><p>Lorem ipsum dolor sit amet, consectetur adipiscing</p></div>
    <div class="grid">
      <div class="col">
        <div class="add-wishlist"><p>Turn conversations<br>into decisions</p><span class="plus"><svg viewBox="0 0 12 12"><use href="#i-plus"/></svg></span><strong>Add Wishlist</strong></div>
        <article class="product-card"><span class="more"></span>
          <div class="product-shot" role="img" aria-label="Light blue water bottle" style="height:120px;background:linear-gradient(180deg,#f2f5f7,#8fb1c4 45%,#7fa3b8)"></div>
          <div class="stars">★★★★★</div><p class="product-name">Lorem Ipsum is simply dummy</p><p class="price">$50.00</p><p class="store">shopmart.com</p>
          <div class="card-actions"><span class="vote"><svg><use href="#i-up"/></svg>4</span><span class="vote"><svg><use href="#i-down"/></svg>0</span><span class="review-btn"><svg><use href="#i-star"/></svg>Review</span></div>
        </article>
      </div>
      <div class="col">
        <article class="product-card"><span class="more"></span>
          <div class="product-shot" role="img" aria-label="Black running sneaker" style="height:60px;background:linear-gradient(180deg,#fff,#d8d8d8 50%,#2b2b2b 75%,#fff)"></div>
          <div class="stars">★★★★★</div><p class="product-name">Lorem Ipsum is simply dummy</p><p class="price">$50.00</p><p class="store">shopmart.com</p>
          <div class="card-actions"><span class="vote"><svg><use href="#i-up"/></svg>4</span><span class="vote"><svg><use href="#i-down"/></svg>0</span><span class="review-btn"><svg><use href="#i-star"/></svg>Review</span></div>
        </article>
        <article class="product-card"><span class="more"></span>
          <div class="product-shot" role="img" aria-label="Black digital camera" style="height:62px;background:radial-gradient(circle at 45% 55%,#2a2a2a 35%,#777 55%,#fff 75%)"></div>
          <div class="stars">★★★★★</div><p class="product-name">Lorem Ipsum is simply dummy</p><p class="price">$50.00</p><p class="store">shopmart.com</p>
          <div class="card-actions"><span class="vote"><svg><use href="#i-up"/></svg>4</span><span class="vote"><svg><use href="#i-down"/></svg>0</span><span class="review-btn"><svg><use href="#i-star"/></svg>Review</span></div>
        </article>
      </div>
    </div>
  </div>
</section>

<!-- Wishlist screen, full -->
<section class="screen screen--wishlist">
  <header class="app-bar">
    <span class="round"><svg><use href="#i-back"/></svg></span>
    <span class="title">Basketlyn</span>
    <div class="bar-actions">
      <span class="round"><svg><use href="#i-info"/></svg></span>
      <span class="round"><svg><use href="#i-user"/></svg></span>
      <span class="round"><svg><use href="#i-chat"/></svg></span>
      <span class="round"><svg><use href="#i-menu"/></svg></span>
    </div>
  </header>
  <div class="body">
    <div class="event-row"><h2>Marco’s 30<sup>th</sup> Birthday</h2><span>@marcob</span></div>
    <div class="hero"><div class="cake" role="img" aria-label="Birthday cake with colourful candles"></div><h3>LOREM IPSUM IS SIMPLY DUM.</h3><p>Lorem ipsum dolor sit amet, consectetur adipiscing</p></div>
    <div class="grid">
      <div class="col">
        <div class="add-wishlist"><p>Turn conversations<br>into decisions</p><span class="plus"><svg viewBox="0 0 12 12"><use href="#i-plus"/></svg></span><strong>Add Wishlist</strong></div>
        <article class="product-card"><span class="more"></span>
          <div class="product-shot" role="img" aria-label="Light blue water bottle" style="height:120px;background:linear-gradient(180deg,#f2f5f7,#8fb1c4 45%,#7fa3b8)"></div>
          <div class="stars">★★★★★</div><p class="product-name">Lorem Ipsum is simply dummy</p><p class="price">$50.00</p><p class="store">shopmart.com</p>
          <div class="card-actions"><span class="vote"><svg><use href="#i-up"/></svg>4</span><span class="vote"><svg><use href="#i-down"/></svg>0</span><span class="review-btn"><svg><use href="#i-star"/></svg>Review</span></div>
        </article>
        <article class="product-card"><span class="more"></span>
          <div class="product-shot" role="img" aria-label="Silver tablet with colourful screen" style="height:88px;background:linear-gradient(120deg,#d8453a,#3a3a48 45%,#c9c9cc 60%,#8f8f94)"></div>
          <div class="stars">★★★★★</div><p class="product-name">Lorem Ipsum is simply dummy</p><p class="price">$50.00</p><p class="store">shopmart.com</p>
          <div class="card-actions"><span class="vote"><svg><use href="#i-up"/></svg>4</span><span class="vote"><svg><use href="#i-down"/></svg>0</span><span class="review-btn"><svg><use href="#i-star"/></svg>Review</span></div>
        </article>
      </div>
      <div class="col">
        <article class="product-card"><span class="more"></span>
          <div class="product-shot" role="img" aria-label="Black running sneaker" style="height:60px;background:linear-gradient(180deg,#fff,#d8d8d8 50%,#2b2b2b 75%,#fff)"></div>
          <div class="stars">★★★★★</div><p class="product-name">Lorem Ipsum is simply dummy</p><p class="price">$50.00</p><p class="store">shopmart.com</p>
          <div class="card-actions"><span class="vote"><svg><use href="#i-up"/></svg>4</span><span class="vote"><svg><use href="#i-down"/></svg>0</span><span class="review-btn"><svg><use href="#i-star"/></svg>Review</span></div>
        </article>
        <article class="product-card"><span class="more"></span>
          <div class="product-shot" role="img" aria-label="Black digital camera" style="height:62px;background:radial-gradient(circle at 45% 55%,#2a2a2a 35%,#777 55%,#fff 75%)"></div>
          <div class="stars">★★★★★</div><p class="product-name">Lorem Ipsum is simply dummy</p><p class="price">$50.00</p><p class="store">shopmart.com</p>
          <div class="card-actions"><span class="vote"><svg><use href="#i-up"/></svg>4</span><span class="vote"><svg><use href="#i-down"/></svg>0</span><span class="review-btn"><svg><use href="#i-star"/></svg>Review</span></div>
        </article>
        <article class="product-card"><span class="more"></span>
          <div class="product-shot" role="img" aria-label="White raglan t-shirt with black sleeves" style="height:88px;background:linear-gradient(90deg,#1e1e1e 0 22%,#e9e9e9 22% 78%,#1e1e1e 78%)"></div>
          <div class="stars">★★★★★</div><p class="product-name">Lorem Ipsum is simply dummy</p><p class="price">$50.00</p><p class="store">shopmart.com</p>
          <div class="card-actions"><span class="vote"><svg><use href="#i-up"/></svg>4</span><span class="vote"><svg><use href="#i-down"/></svg>0</span><span class="review-btn"><svg><use href="#i-star"/></svg>Review</span></div>
        </article>
      </div>
    </div>
  </div>
  <nav class="tab-bar">
    <span class="tab is-active"><svg><use href="#i-home"/></svg>Home</span>
    <span class="tab"><svg><use href="#i-store"/></svg>Stores</span>
    <span class="tab"><svg><use href="#i-search"/></svg>Discover</span>
    <span class="tab"><svg><use href="#i-bubble"/></svg>Chat</span>
  </nav>
</section>

<!-- Stores screen -->
<section class="screen screen--stores">
  <header class="app-bar">
    <span class="round"><svg><use href="#i-back"/></svg></span>
    <span class="title">Basketlyn</span>
    <div class="bar-actions">
      <span class="round"><svg><use href="#i-info"/></svg></span>
      <span class="round"><svg><use href="#i-user"/></svg></span>
      <span class="round"><svg><use href="#i-chat"/></svg></span>
      <span class="round"><svg><use href="#i-menu"/></svg></span>
    </div>
  </header>
  <div class="body">
    <div class="intro">
      <h2>Find your favorite items</h2>
      <h3>from our retail partners!</h3>
      <p>Find products from any retailer, add them to your WishList with the Share button, and share it with friends and family. Start your shared WishList now!</p>
      <span class="demo-btn"><i></i>Watch Demo Video</span>
    </div>
    <h2 class="section-head">Favorites</h2>
    <div class="brands">
      <div class="brand-tile" style="--c:#d94a3d"><i></i><span>Crestfield</span></div>
      <div class="brand-tile" style="--c:#2f55b8"><i></i><span>Steadybar</span></div>
      <div class="brand-tile" style="--c:#e2a22a"><i></i><span>Rosalio</span></div>
      <div class="brand-tile" style="--c:#2d4fb0"><i></i><span>Cocoro</span></div>
    </div>
    <div class="brands">
      <div class="brand-tile" style="--c:#d94a3d"><i></i><span>Crestfield</span></div>
      <div class="brand-tile" style="--c:#2f55b8"><i></i><span>Steadybar</span></div>
      <div class="brand-tile" style="--c:#e2a22a"><i></i><span>Rosalio</span></div>
      <div class="brand-tile" style="--c:#2d4fb0"><i></i><span>Cocoro</span></div>
    </div>
    <h2 class="letter-head">A</h2>
    <div class="brands">
      <div class="brand-tile" style="--c:#c8322e"><i></i><span>Morningfield</span></div>
      <div class="brand-tile" style="--c:#444"><i></i><span>Sunny Scoop</span></div>
      <div class="brand-tile" style="--c:#5a3a2a"><i></i><span>Hartwell</span></div>
      <div class="brand-tile" style="--c:#d83a34"><i></i><span>Dalora</span></div>
    </div>
    <div class="brands">
      <div class="brand-tile" style="--c:#2b56b5"><i></i><span>Honey Nook</span></div>
      <div class="brand-tile" style="--c:#d64136"><i></i><span>Postwick</span></div>
      <div class="brand-tile" style="--c:#3c6fb3"><i></i><span>Nestora</span></div>
      <div class="brand-tile" style="--c:#6b2f22"><i></i><span>dotties</span></div>
    </div>
  </div>
  <nav class="tab-bar">
    <span class="tab"><svg><use href="#i-home"/></svg>Home</span>
    <span class="tab is-active"><svg><use href="#i-store"/></svg>Stores</span>
    <span class="tab"><svg><use href="#i-search"/></svg>Discover</span>
    <span class="tab"><svg><use href="#i-bubble"/></svg>Chat</span>
  </nav>
</section>

<!-- Discover screen -->
<section class="screen screen--discover">
  <header class="app-bar">
    <span class="round"><svg><use href="#i-back"/></svg></span>
    <span class="title">Basketlyn</span>
    <div class="bar-actions">
      <span class="round"><svg><use href="#i-info"/></svg></span>
      <span class="round"><svg><use href="#i-user"/></svg></span>
      <span class="round"><svg><use href="#i-chat"/></svg></span>
      <span class="round"><svg><use href="#i-menu"/></svg></span>
    </div>
  </header>
  <div class="search-band"><div class="search-field">Search for Wishlist<svg viewBox="0 0 12 12"><use href="#i-search"/></svg></div></div>
  <div class="body">
    <div class="category"><h2>Automotive</h2><span class="view-all">View All</span></div>
    <div class="group-row">
      <div class="group-card" role="img" aria-label="Silver hatchback car on a road" style="background:linear-gradient(180deg,#8a9098,#4b525a 60%,#2a2e33)"><span class="tag">Invite</span><span class="mark"></span><div class="members"><i></i><i></i><span>93 members</span></div><p>Lorem ipsum dolor sit amet, consecte</p></div>
      <div class="group-card" role="img" aria-label="White SUV in green countryside" style="background:linear-gradient(180deg,#5f7a55,#8d9a84 50%,#3c4a35)"><span class="tag">Join</span><span class="mark"></span><div class="members"><i></i><i></i><span>93 members</span></div><p>Lorem ipsum dolor sit amet, consecte</p></div>
      <div class="group-card peek" style="background:#5a5f62"></div>
    </div>
    <div class="category"><h2>Beauty &amp; Healthy</h2><span class="view-all">View All</span></div>
    <div class="group-row">
      <div class="group-card" role="img" aria-label="Beauty portrait among green leaves" style="background:linear-gradient(135deg,#1f3a5a,#3a6a6a 50%,#b08466)"><span class="tag">Invite</span><span class="mark"></span><div class="members"><i></i><i></i><span>93 members</span></div><p>Lorem ipsum dolor sit amet, consecte</p></div>
      <div class="group-card" role="img" aria-label="Skincare portrait with soft foliage" style="background:linear-gradient(135deg,#7c8a5a,#d9b39a 55%,#c88c74)"><span class="tag">Invite</span><span class="mark"></span><div class="members"><i></i><i></i><span>93 members</span></div><p>Lorem ipsum dolor sit amet, consecte</p></div>
      <div class="group-card peek" style="background:#4d4a45"></div>
    </div>
    <div class="category"><h2>Wellness</h2><span class="view-all">View All</span></div>
    <div class="group-row">
      <div class="group-card" style="background:#9aa6b0"></div>
      <div class="group-card" style="background:#a9b4ad"></div>
    </div>
  </div>
  <nav class="tab-bar" style="position:absolute;left:0;right:0;bottom:0">
    <span class="tab"><svg><use href="#i-home"/></svg>Home</span>
    <span class="tab"><svg><use href="#i-store"/></svg>Stores</span>
    <span class="tab is-active"><svg><use href="#i-search"/></svg>Discover</span>
    <span class="tab"><svg><use href="#i-bubble"/></svg>Chat</span>
  </nav>
</section>
</body>
</html>
```